I would like a formal monogram with LM and Lorna Mabbery Interiors written somehow. this a a new interior design company based in Dallas. My favorite colors is Halvorne blue with gold or white writing or some variation of.
back: Lorna Mabbery
214-630-4182
lorna.mabbery@quillpost.example
www.lornamabberyinteriors.example

```html
<!DOCTYPE html>
<html lang="en">
<head>
<meta charset="utf-8">
<title>Lorna Mabbery Interiors – Business Card</title>
<link rel="stylesheet" href="https://fonts.googleapis.com/css2?family=Cinzel:wght@400&family=Montserrat:wght@500;700&display=swap">
<style>
  :root {
    --backdrop: #2b2b2d;
    --halvorne-blue: #87cbea;
    --accent-teal: #3eb3d3;
    --card-white: #ffffff;
    --ink: #1f1f22;
    --rule-blue: #a9dcef;
  }
  * { margin: 0; padding: 0; box-sizing: border-box; }
  html, body {
    width: 1200px;
    height: 1186px;
    overflow: hidden;
    background: var(--backdrop);
  }
  .sheet {
    position: relative;
    width: 1200px;
    height: 1186px;
  }
  .card {
    position: absolute;
    left: 150px;
    width: 900px;
    height: 514px;
    border-radius: 34px;
    overflow: hidden;
  }
  .card--front { top: 56px; background: var(--halvorne-blue); }
  .card--back { top: 616px; background: var(--card-white); }

  .wordmark {
    font-family: "Cinzel", serif;
    font-weight: 400;
    text-align: center;
    line-height: 1.15;
    display: flex;
    flex-direction: column;
    align-items: center;
    gap: 14px;
  }
  .wordmark__dot {
    width: 18px;
    height: 18px;
    border-radius: 50%;
  }
  .card--front .wordmark {
    position: absolute;
    left: 0; right: 0; top: 150px;
    color: var(--card-white);
    font-size: 54px;
    letter-spacing: 2px;
  }
  .card--front .wordmark__dot { background: var(--card-white); }

  .card--back .wordmark {
    position: absolute;
    right: 60px; top: 70px;
    width: 400px;
    color: var(--halvorne-blue);
    font-size: 34px;
    letter-spacing: 1.5px;
  }
  .card--back .wordmark__dot { background: var(--halvorne-blue); }

  .back__rule {
    position: absolute;
    left: 40px; right: 40px; top: 262px;
    height: 1.5px;
    background: var(--rule-blue);
  }
  .contact {
    position: absolute;
    left: 60px; bottom: 56px;
    font-family: "Montserrat", sans-serif;
  }
  .contact__name {
    color: var(--accent-teal);
    font-weight: 700;
    font-size: 38px;
    margin-bottom: 14px;
  }
  .contact__list { list-style: none; }
  .contact__item {
    display: flex;
    align-items: center;
    gap: 16px;
    color: var(--ink);
    font-weight: 500;
    font-size: 22px;
    line-height: 34px;
  }
  .contact__icon { width: 20px; height: 20px; flex: none; }
</style>
</head>
<body>
<main class="sheet">
  <section class="card card--front" aria-label="Card front">
    <div class="wordmark">
      <span class="wordmark__dot"></span>
      <span>Lorna Mabbery<br>Interiors</span>
    </div>
  </section>

  <section class="card card--back" aria-label="Card back">
    <div class="wordmark">
      <span class="wordmark__dot"></span>
      <span>Lorna Mabbery<br>Interiors</span>
    </div>
    <div class="back__rule"></div>
    <div class="contact">
      <p class="contact__name">Lorna Mabbery</p>
      <ul class="contact__list">
        <li class="contact__item">
          <svg class="contact__icon" viewBox="0 0 20 20" aria-hidden="true"><path fill="#3eb3d3" d="M4 2h4l1.5 4-2.2 1.4a11 11 0 0 0 5.3 5.3L14 10.5l4 1.5v4a2 2 0 0 1-2 2A16 16 0 0 1 2 4a2 2 0 0 1 2-2z"/></svg>
          <span>214-630-4182</span>
        </li>
        <li class="contact__item">
          <svg class="contact__icon" viewBox="0 0 20 20" aria-hidden="true"><rect x="1" y="4" width="18" height="12" rx="1.5" fill="#3eb3d3"/><path d="M2 5l8 6 8-6" fill="none" stroke="#fff" stroke-width="1.5"/></svg>
          <span>lorna.mabbery@quillpost.example</span>
        </li>
        <li class="contact__item">
          <svg class="contact__icon" viewBox="0 0 20 20" aria-hidden="true"><circle cx="10" cy="10" r="8.5" fill="#3eb3d3"/><path d="M1.5 10h17M10 1.5c-4 4.5-4 12.5 0 17M10 1.5c4 4.5 4 12.5 0 17" fill="none" stroke="#fff" stroke-width="1.2"/></svg>
          <span>www.lornamabberyinteriors.example</span>
        </li>
      </ul>
    </div>
  </section>
</main>
</body>
</html>
```